Legal Service Estimated Retainer and Average Case Value

We need an 11x14 flyer that contains the standard retainers and average cost be case, both provided in documents, for each case type we handle. We need the information displayed, preferably in a way that makes the information readable but less troubling to a client shocked at price of litigation. We need one sheet with the retainers and average case value merged into one table.

Target Market(s)

Potential Clients

Font styles to use
Serif
Sans Serif

```html
<!DOCTYPE html>
<html lang="en">
<head>
<meta charset="utf-8">
<title>Retainers and Average Case Costs</title>
<link rel="stylesheet" href="https://fonts.googleapis.com/css2?family=Cinzel:wght@400;700&family=Roboto:wght@500;700&display=swap">
<style>
  :root{
    --page-bg:#bfbfbf;
    --paper:#ffffff;
    --brand-blue:#1b4594;
    --head-gray:#8f8f8f;
    --row-alt:#dedede;
    --rule:#a9a9a9;
    --frame:#1f1f1f;
    --ink:#111111;
  }
  *{box-sizing:border-box;margin:0;padding:0}
  html,body{width:1200px;height:1200px;overflow:hidden;background:var(--page-bg)}
  .flyer{
    position:absolute;left:144px;top:20px;width:912px;height:1160px;
    background:var(--paper);overflow:hidden;
  }
  .hero{
    position:absolute;left:0;top:0;width:912px;height:238px;
    background:linear-gradient(100deg,#6b5b50 0%,#7a736d 38%,#86817c 60%,#6a5d55 100%);
  }
  .hero-band{position:absolute;left:0;top:245px;width:912px;height:12px;background:var(--brand-blue)}
  .firm-name{
    position:absolute;left:0;top:78px;width:912px;text-align:center;
    font-family:"Cinzel",serif;font-weight:400;color:#ffffff;line-height:1;
  }
  .firm-name .kicker{display:block;font-size:17px;letter-spacing:1px;margin-bottom:8px}
  .firm-name .name{display:block;font-size:38px;letter-spacing:1px}
  .title{
    position:absolute;left:0;top:288px;width:912px;text-align:center;
    font-family:"Cinzel",serif;font-weight:700;font-size:29px;color:var(--brand-blue);letter-spacing:.5px;
  }
  .footer{
    position:absolute;left:0;top:1007px;width:912px;height:153px;background:var(--brand-blue);
  }
  .contact{
    position:absolute;left:0;width:912px;text-align:center;color:#fff;
    font-family:"Roboto",sans-serif;font-weight:700;
  }
  .contact-line{top:1071px;font-size:25px;display:flex;justify-content:center;align-items:center;gap:10px}
  .contact-web{top:1107px;font-size:24px}
  .phone-icon{width:20px;height:20px;display:block}
  .rates{
    position:absolute;left:18px;top:354px;width:876px;
    border-collapse:collapse;border:2px solid var(--frame);
    font-family:"Roboto",sans-serif;background:var(--paper);
  }
  .rates th{
    background:var(--head-gray);color:#fff;font-weight:500;font-size:25px;height:35px;
    border-left:1px solid var(--rule);
  }
  .rates td{
    height:51px;text-align:center;font-weight:700;font-size:13.5px;color:var(--ink);
    line-height:1.2;border-left:1px solid var(--rule);padding:0 6px;
  }
  .rates tr:nth-child(even) td{background:var(--row-alt)}
  .col-case{width:203px}.col-cost{width:227px}.col-case2{width:226px}.col-cost2{width:220px}
</style>
</head>
<body>
  <div class="flyer">
    <div class="hero" role="img" aria-label="Photo of hands signing a legal document with a pen"></div>
    <div class="firm-name"><span class="kicker">The Law Office of</span><span class="name">DANIEL M WHITAKER</span></div>
    <div class="hero-band"></div>

    <h1 class="title">Retainers and average Case Costs:</h1>

    <div class="footer"></div>

    <table class="rates">
      <thead>
        <tr>
          <th class="col-case">Avarage Case</th><th class="col-cost">Cost</th>
          <th class="col-case2">Avarage Case</th><th class="col-cost2">Cost</th>
        </tr>
      </thead>
      <tbody>
        <tr><td>(3301 C)</td><td>Retainer: $2,000</td><td>Custody Contempt/Modification</td><td>$5,000 - $8,000</td></tr>
        <tr><td>(3301 D)</td><td>Retainer: $2,500</td><td>Custody Initial Order</td><td>$4,000 - $7,000</td></tr>
        <tr><td>Custody</td><td>Retainer: $3,500</td><td>Custody &amp; Support</td><td>$5,000 - $8,000</td></tr>
        <tr><td>Equitable Distribution</td><td>Retainer: $3,500</td><td>Support</td><td>$2,000 - $4,000</td></tr>
        <tr><td>Support</td><td>Retainer: $3,000</td><td>Divorce (3301c)</td><td>$1,500 - $3,000</td></tr>
        <tr><td>Custody and Support</td><td>Retainer: $3,500</td><td>Divorce (3301d)</td><td>$2,000 - $3,000</td></tr>
        <tr><td>Equitable Distribution<br>and Support</td><td>Retainer: $3,500</td><td>Protection from Abuse</td><td>$1,500 - $3,000</td></tr>
        <tr><td>Equitable Distribution<br>and Custody</td><td>Retainer: $5,000</td><td>Divorce &amp; Custody</td><td>$5,000 - $8,000</td></tr>
        <tr><td>Equitable Distribution,<br>Custody and Support</td><td>Retainer: $3,500</td><td>Divorce &amp; Equitable Distribution</td><td>$6,000 - $10,000</td></tr>
        <tr><td>Custody Initial Order</td><td>Retainer: $3,000</td><td>Divorce, Custody &amp; Support</td><td>$8,000 - $12,000</td></tr>
        <tr><td>Custody Modification</td><td>Retainer: $3,500</td><td>Divorce, Equitable Distribution<br>&amp; Custody</td><td>$10,000 - $15,000</td></tr>
        <tr><td>Custody and Support</td><td>Retainer: $3,000</td><td>Divorce, Equitable Distribution<br>&amp; Support</td><td>$8,000 - $12,000</td></tr>
        <tr><td>(PFA) Protection<br>From Abuse</td><td>: $2,000 Paid In Full</td><td>Divorce, Equitable Distribution,<br>Custody &amp; Support</td><td>$12,000 - $15,000</td></tr>
      </tbody>
    </table>

    <div class="contact contact-line">
      <span>Complimentary Consultations</span>
      <svg class="phone-icon" viewBox="0 0 20 20" aria-hidden="true">
        <rect x="0" y="0" width="20" height="20" rx="4" fill="#fff"/>
        <path d="M6 4.5c.6-.4 1.3-.2 1.6.4l1 1.9c.3.5.1 1.1-.3 1.4l-.8.6c.5 1.4 1.4 2.5 2.7 3.3l.7-.7c.4-.4 1-.5 1.5-.1l1.8 1.2c.5.4.6 1.1.2 1.6l-.8 1c-.6.7-1.6.9-2.5.5-3-1.3-5.2-3.9-6.1-7-.2-.9.1-1.8.8-2.3z" fill="var(--brand-blue)"/>
      </svg>
      <span>555.014.2286</span>
    </div>
    <div class="contact contact-web">www.whitakerfamilylaw.com</div>
  </div>
</body>
</html>
```